Marketing Business Card Design

I am, launching a marketing business where I will contract to market hospitality. I want something funky and fun to go with the name Pickle Pail

Industry/Entity Type

Marketing

Contact Information for Business Card

Marla Tennant-Greaves
Pickle Pail
Mobile: +61 2 407 392654
Email: marla@picklepail.com.au

Requirements
Must have
• Fun and modern
Should not have
• Not conservative

```html
<!DOCTYPE html>
<html lang="en">
<head>
<meta charset="utf-8">
<title>Pickle Pail – Business Card</title>
<link rel="stylesheet" href="https://fonts.googleapis.com/css2?family=Quicksand:wght@500;700&display=swap">
<style>
  :root {
    --paper: #ffffff;
    --brand-red: #8b2323;
    --rule-red: #ed1c24;
    --peach-soft: #fde4d8;
    --peach-mid: #f6b49b;
    --panel-light: #e8eff7;
    --panel-sky: #00a0dc;
    --panel-deep: #1c3f94;
    --panel-edge: #7fd0f2;
    --ink-navy: #2e3192;
    --accent-yellow: #f2ea00;
    --text-white: #ffffff;
  }
  html, body {
    margin: 0;
    padding: 0;
    width: 1200px;
    height: 700px;
    overflow: hidden;
    background: var(--paper);
  }
  .card {
    position: relative;
    width: 1200px;
    height: 700px;
    background: var(--paper);
    font-family: "Quicksand", sans-serif;
  }
  .pattern-field {
    position: absolute;
    left: 25px;
    top: 25px;
    width: 1151px;
    height: 382px;
  }
  .brand {
    position: absolute;
    left: 200px;
    top: 25px;
    height: 382px;
    display: flex;
    align-items: center;
    gap: 36px;
  }
  .brand-dot {
    width: 110px;
    height: 110px;
    border-radius: 50%;
    background: var(--brand-red);
  }
  .brand-name {
    margin: 0;
    font-weight: 700;
    font-size: 118px;
    line-height: 1;
    color: var(--brand-red);
    letter-spacing: -1px;
  }
  .rule {
    position: absolute;
    left: 25px;
    top: 407px;
    width: 1151px;
    height: 12px;
    background: var(--rule-red);
  }
  .contact-panel {
    position: absolute;
    left: 25px;
    top: 419px;
    width: 1151px;
    height: 255px;
    box-sizing: border-box;
    border: 4px solid var(--panel-edge);
    border-top: none;
    background: linear-gradient(90deg, var(--panel-light) 0%, var(--panel-sky) 45%, var(--panel-deep) 100%);
  }
  .person {
    position: absolute;
    left: 67px;
    top: 40px;
    display: flex;
    align-items: center;
  }
  .person-name {
    font-weight: 500;
    font-size: 44px;
    color: var(--ink-navy);
    letter-spacing: 1px;
  }
  .person-divider {
    width: 4px;
    height: 58px;
    background: var(--text-white);
    margin: 0 10px 0 20px;
  }
  .person-surname {
    font-weight: 500;
    font-size: 34px;
    color: var(--accent-yellow);
    margin-top: 8px;
  }
  .mobile, .email {
    position: absolute;
    top: 168px;
    margin: 0;
    font-weight: 500;
    font-size: 26px;
    letter-spacing: 0.5px;
  }
  .mobile {
    left: 67px;
    color: var(--ink-navy);
  }
  .email {
    right: 70px;
    color: var(--text-white);
  }
</style>
</head>
<body>
  <main class="card">
    <svg class="pattern-field" viewBox="0 0 1151 382" role="img" aria-label="Decorative pattern of overlapping peach spirals on white">
      <defs>
        <radialGradient id="peachWash" cx="50%" cy="50%" r="75%">
          <stop offset="0%" stop-color="#fde4d8"/>
          <stop offset="100%" stop-color="#f6b49b"/>
        </radialGradient>
      </defs>
      <rect width="1151" height="382" fill="url(#peachWash)"/>
    </svg>

    <div class="brand">
      <span class="brand-dot"></span>
      <h1 class="brand-name">pickle pail</h1>
    </div>

    <div class="rule"></div>

    <section class="contact-panel">
      <div class="person">
        <span class="person-name">Marla Tennant</span>
        <span class="person-divider"></span>
        <span class="person-surname">Greaves</span>
      </div>
      <p class="mobile">Mobile: +61 2 407 392654</p>
      <p class="email">Email: marla@picklepail.com.au</p>
    </section>
  </main>
</body>
</html>
```